Wallpaper für Partner für ganzheitliche IT-Infrastruktur-Lösungen
Zielgruppe
Wir sind Partner für ganzheitliche IT-Infrastruktur-Lösungen. Wir übernehmen technische Verantwortung für stabile, sichere und wirtschaftliche IT‑Systeme – von der Konzeption über den Betrieb bis zur langfristigen Betreuung. Unsere Zielgruppe sind kleine und mittelständische Unternehmen und Organisationen, die ihre IT als strategischen Erfolgsfaktor verstehen und Wert auf durchdachte Gesamtlösungen statt auf Stückwerk legen.
Aufgabenstellung
Es soll ein Wallpaper erstellt werden, das die bestehende CI ergänzt.
Das Design soll Verantwortung, Kompetenz und Verlässlichkeit ausstrahlen. Gesucht ist eine professionelle, aber zugängliche Optik, die ganzheitliches Denken und technische Stabilität vermittelt. Der Stil sollte modern, aber zeitlos sein – keine kurzlebigen Trends oder oberflächliche Tech-Klischees. Wichtig sind klare Strukturen und hochwertige Ästhetik, die Vertrauen schafft. Das NK-VR-Logo oder -Icon soll harmonisch in das Design integriert werden. Technische Anforderungen: Der Wallpaper muss sowohl im 16:9- als auch im 9:16-Format funktionieren und vollständig als Vektorgrafik ohne Rastereffekte geliefert werden.

```html
<!DOCTYPE html>
<html lang="de">
<head>
<meta charset="utf-8">
<title>NK-VR GmbH – Wallpaper</title>
<link rel="stylesheet" href="https://fonts.googleapis.com/css2?family=Titillium+Web:wght@300;700&display=swap">
<style>
  :root {
    --stage: #e0e0e0;
    --paper: #ffffff;
    --blush: #f7ebe4;
    --rose: #e3a3a6;
    --brand-red: #b71c24;
    --ink-grey: #68686a;
  }
  html, body {
    margin: 0;
    padding: 0;
    width: 1200px;
    height: 1117px;
    overflow: hidden;
    background: var(--stage);
  }
  .wallpaper {
    position: absolute;
    left: 318px;
    top: 57px;
    width: 564px;
    height: 1002px;
    display: block;
  }
  .brand-name { font-family: "Titillium Web", sans-serif; font-weight: 300; fill: var(--ink-grey); }
  .service-label {
    font-family: "Titillium Web", sans-serif;
    font-weight: 700;
    font-size: 40px;
    fill: var(--ink-grey);
    text-anchor: middle;
  }
  .web-address {
    font-family: "Titillium Web", sans-serif;
    font-weight: 700;
    font-size: 30px;
    letter-spacing: 14px;
    fill: var(--paper);
    text-anchor: middle;
  }
  .card-face { fill: var(--brand-red); }
  .card-base { fill: var(--rose); }
  .card-gap { fill: var(--paper); }
  .icon-line { fill: none; stroke: var(--paper); stroke-width: 9; stroke-linecap: round; stroke-linejoin: round; }
  .icon-fill { fill: var(--paper); }
  .dot { fill: var(--brand-red); }
</style>
</head>
<body>
<svg class="wallpaper" viewBox="527 95 934 1660" xmlns="http://www.w3.org/2000/svg" aria-label="NK-VR GmbH Wallpaper">
  <!-- base -->
  <rect x="527" y="95" width="934" height="1660" fill="var(--paper)"/>

  <!-- top band with tabs -->
  <rect x="527" y="95" width="934" height="85" fill="var(--blush)"/>
  <rect x="712" y="116" width="161" height="100" rx="30" fill="var(--paper)"/>
  <rect x="1120" y="116" width="160" height="100" rx="30" fill="var(--paper)"/>

  <!-- brand -->
  <g class="brand">
    <rect x="622" y="300" width="108" height="108" rx="8" fill="var(--brand-red)"/>
    <text class="brand-name" x="790" y="408" font-size="180">NK-VR</text>
    <text class="brand-name" x="1282" y="409" font-size="52">GmbH</text>
  </g>

  <!-- decorative blocks -->
  <path d="M527 644 H636 A55 55 0 0 1 691 699 V1029 A55 55 0 0 1 636 1084 H527 Z" fill="var(--rose)"/>
  <path d="M1461 1148 H1408 A50 50 0 0 0 1358 1198 V1342 A50 50 0 0 0 1408 1392 H1461 Z" fill="var(--rose)"/>

  <!-- dot grids -->
  <g class="dot-grid">
    <rect class="dot" x="1352" y="515" width="9" height="9"/><rect class="dot" x="1375" y="515" width="9" height="9"/><rect class="dot" x="1397" y="515" width="9" height="9"/><rect class="dot" x="1420" y="515" width="9" height="9"/><rect class="dot" x="1442" y="515" width="9" height="9"/>
    <rect class="dot" x="1352" y="539" width="9" height="9"/><rect class="dot" x="1375" y="539" width="9" height="9"/><rect class="dot" x="1397" y="539" width="9" height="9"/><rect class="dot" x="1420" y="539" width="9" height="9"/><rect class="dot" x="1442" y="539" width="9" height="9"/>
    <rect class="dot" x="541" y="1341" width="9" height="9"/><rect class="dot" x="563" y="1341" width="9" height="9"/><rect class="dot" x="585" y="1341" width="9" height="9"/><rect class="dot" x="607" y="1341" width="9" height="9"/>
    <rect class="dot" x="541" y="1365" width="9" height="9"/><rect class="dot" x="563" y="1365" width="9" height="9"/><rect class="dot" x="585" y="1365" width="9" height="9"/><rect class="dot" x="607" y="1365" width="9" height="9"/>
  </g>

  <!-- service: managed services -->
  <g class="service-card">
    <rect class="card-base" x="915" y="636" width="173" height="50" rx="20"/>
    <rect class="card-gap" x="915" y="630" width="173" height="38" rx="14"/>
    <rect class="card-face" x="920" y="496" width="163" height="162" rx="14"/>
    <rect class="icon-line" x="986" y="535" width="32" height="24" rx="5"/>
    <path class="icon-line" d="M1002 559 V576 M946 576 H1057 M973 576 V594 M1027 576 V594"/>
    <rect class="icon-line" x="958" y="596" width="31" height="24" rx="5"/>
    <rect class="icon-line" x="1012" y="596" width="31" height="24" rx="5"/>
    <text class="service-label" x="1002" y="748">MANAGED SERVICES</text>
  </g>

  <!-- service: managed infrastructure -->
  <g class="service-card">
    <rect class="card-base" x="919" y="980" width="173" height="50" rx="20"/>
    <rect class="card-gap" x="919" y="974" width="173" height="38" rx="14"/>
    <rect class="card-face" x="924" y="840" width="163" height="162" rx="14"/>
    <rect class="icon-fill" x="956" y="871" width="100" height="42" rx="21"/>
    <rect class="icon-fill" x="956" y="929" width="100" height="42" rx="21"/>
    <circle cx="1018" cy="892" r="6" fill="var(--brand-red)"/><circle cx="1036" cy="892" r="6" fill="var(--brand-red)"/>
    <circle cx="1018" cy="950" r="6" fill="var(--brand-red)"/><circle cx="1036" cy="950" r="6" fill="var(--brand-red)"/>
    <text class="service-label" x="993" y="1088">MANAGED INFRASTRUKTUR</text>
  </g>

  <!-- service: consulting -->
  <g class="service-card">
    <rect class="card-base" x="919" y="1334" width="173" height="50" rx="20"/>
    <rect class="card-gap" x="919" y="1328" width="173" height="38" rx="14"/>
    <rect class="card-face" x="924" y="1194" width="163" height="162" rx="14"/>
    <path class="icon-fill" d="M1006 1224 A33 33 0 0 1 1029 1281 C1023 1288 1022 1292 1022 1298 H990 C990 1292 989 1288 983 1281 A33 33 0 0 1 1006 1224 Z"/>
    <path class="icon-fill" d="M989 1306 H1023 V1312 A17 17 0 0 1 989 1312 Z"/>
    <path d="M986 1254 A20 20 0 0 1 1002 1238" fill="none" stroke="var(--brand-red)" stroke-width="5" stroke-linecap="round"/>
    <path class="icon-line" d="M954 1230 L964 1236 M952 1258 H964 M954 1284 L964 1278 M1058 1230 L1048 1236 M1060 1258 H1048 M1058 1284 L1048 1278" stroke-width="7"/>
    <text class="service-label" x="993" y="1454">IT-CONSULTING</text>
  </g>

  <!-- footer band -->
  <path d="M527 1536 H580 A56 56 0 0 1 636 1592 V1596 A55 55 0 0 0 691 1651 H866 A56 56 0 0 0 922 1595 V1592 A56 56 0 0 1 978 1536 H1305 A57 57 0 0 1 1362 1593 A58 58 0 0 0 1420 1651 H1461 V1755 H527 Z" fill="var(--brand-red)"/>
  <text class="web-address" x="1155" y="1627">NK-VR.COM</text>
</svg>
</body>
</html>
```